Mobile Repair Service on location needs a Web Design

We are starting a new mobile device repair service called Gadget Haven and our website needs a design!

Hello Designers!
First, we'd like to make clear this is more than a simple web design contest, we want the designers to create an idea. We want someone who can create the whole theme of the service's we provide. We want someone that can help design our visual branding, help us communicate a sentiment. And we are willing to pay for that.

Who are we?
Our company is based in Rotterdam, the Netherlands. We provide different services for all kinds of electronic devices. The kind of services we provide are, among other things, installations of hardware and software and the repair of broken or malfunctioning devices.
We are starting a new service that offers mobile device repairs on location, be it at the home of our customers, their office, or any other place. Just give us the address and we will come to you for the repair job. This is also our main USP. We have multiple skilled engineers who drive trough the country on a daily basis and can be on location within a working day. Repair is done immediately onsite while the customer waits. At this stage we will start with the smartphone product-group within the mobile devices. In a second phase we might also add tablets.
People don't want to be without their phone for weeks because of some parts that needed to be ordered by a repair center they had to sent their phone to. We offer a fully functional mobile repair center in the form of specially customized vans. These vans have all the tools and utilities needed by our engineers to safely repair your mobile device. Your phone is being repaired directly in front of you, the next business-day, on a location you desire.

For this new service we are creating a website called Gadget Haven. The website needs a story and matching design and this is where you come in. We are not looking for a simple template design we can get from any place. We need a story. We want you to create an idea, build a unique theme or vision that helps sell the product/service. This goes beyond the design of the website. We need the whole package, the design you are creating needs to have returning elements like icons, color use, images, maybe even characters etc. You name it! There needs to be a common thread in the design so we can reuse elements in, for example, the email templates, the work order or receipt we give to our customers (we may contact the winner of the contest to design these for us as well!).

The name 'Gadget Haven' is chosen. Haven (short for rehabilitate) has a bold and playful tone to it and the design needs to reflect the name. So we're looking for a somewhat playful and cheeky design. Definitely not too serious and definitely modern. We already got a logo that we love and that fit's this description (see attached design documents for the logo). It's bold, powerful and fun. Our web design needs to reflect this as well and has to fit in with our logo.
We would really like it if the design somehow incorporates elements that highlight our unique selling points (repairs on location, we come to you etc.). We would really like some form of story telling in the design. Think clumsy people breaking their phones. Teenagers in tears because they have no access to their friends. People nowadays have the need to always be 'connected'. What happens when your phone is broken or malfunctioning? We're handling tech, we are nerds and a little bit weird, but we're professionals and here to help you with your problem. The sentiment Wire Troop tries to communicate is something we really like. We're looking for fresh idea's, anything goes!

In an overview all Unique Selling Points of the Gadget haven service:
- Professional service on location. Don’t ship to us we will come to you!
- Clear pricing upfront. No hidden cost.
- Next business-day repair.
- Backed by a professional call center open 12 hours a day and open on a Saturday as well
- Backed by a professional repair center with more then 12 years of experience
- Repair is done by certified engineers
- 1 year warranty on the repair

The process:
The main function of our website will be for customers to make a repair request. A customer will visit our website and can make a repair request immediately by going through a 'request-order-flow'. In this flow he or she will need to fill in some forms and can select wich type/model/brand of mobile device he or she has and what parts need to be repaired. After a request is placed we will call the customer back (within an hour) for a short intake and to set a date/time and location. Our engineer will meet the customer at the specified location and will repair the device onsite in one of our mobile repair centers, which is a specialized van equipped with all the tools needed for device restorations.
So in short the steps are:
- Choose your device and repair job
- Place the order
- Get a callback within the hour
- Set date and location
- We will come to you.

Website functionality:
Our website is our main form of communication. So the sentiment we want to communicate needs be reflected in the design. We need a main/front page designed (preferably a long scrolling page design) containing:
1. Customers will be able to request a repair job directly on our website. So there will need to be a prominent button/link at the top of our main page that will bring the customer to this 'request-order-flow'. This is the main flow which needs to be full focus on the front page. All other items are secondary.
2. The general information of who we are and what we do, and why the customer should choose us. Preferably in short bullet-point type keywords/sentences with icons or other visual cues. See our unique selling points to get an idea of the information that will be displayed here.
3. There needs to be a section that will explain the process (see above) of a repair request step-by- step, again in brief short key sentences and with (custom) icons.
4. There needs to be a section that explains to the customer he/she can always contact us if they are not sure what the problem is with their device, and for this reason are not sure what repair request they should order.
5. We want to implement some functionality that display customer ratings or customer reviews. So there needs to be room for some kind of widget of plugin we're going to implement which shows these reviews.
6. A 'For business section' where we will explain all the options we provide for corporate clients.
7. Social media links.
8. There needs to be a menu with buttons that leads to the all sections described in the previous points.

For now, we need a design for our front page. In the second phase, when we have picked our winner, we may ask the winner to design the page(s) for our request workflow as well.

EDIT:
Finally, we have a very specific order in mind for the different segments of our website. We would like you to add some more segments that were not in our original brief as well:

1. Top header with order/request button. (should instantly make clear our main USP, we do repairs on location)
2. Our process
3. Our unique selling points / why choose us
4. The kind of repairs we do (broken screens, broken batteries, water damage, broken camera's, no sound etc.)
5. A 'meet our team' section, where we introduce some of our engineers
6. A 'contact us for any questions' section/
7. Testimonials/user reviews
8. A section where we show key performance indicators
9. 'For businesses' sections
10.'Subscribe for newsletter' field
11. Social media buttons

Industry/Entity Type

It Service

Number of Pages Required

1 page

Font styles to use
Sans Serif

Requirements
Must have
• a main/front page, design only
• custom icons/images for banners, adverts online and in print (high res)
Nice to have
• Storytelling in our design.
• Design that fits with our brand new logo.
• Elements like icons to have a flat design.
• Keep in mind that the website will need to be responsive when designing! (Ideally provide an example of the mobile design as well)
• Create a fun and trustworthy feeling.

```html
<!DOCTYPE html>
<html lang="en">
<head>
<meta charset="utf-8">
<title>Gadget Haven – Mobile Repair On Location</title>
<link href="https://fonts.googleapis.com/css2?family=Montserrat:wght@400;500;600;700;800&display=swap" rel="stylesheet">
<style>
:root{
  --orange:#f7931e;
  --orange-dark:#e07f0c;
  --blue:#1e8ff5;
  --green:#3cc23c;
  --ink:#1c1c1c;
  --ink-soft:#2a2a2a;
  --sky:#e4f3fa;
  --navy:#1d3557;
  --grey:#8a8f95;
  --line:#d9dde1;
  --white:#ffffff;
}
*{box-sizing:border-box;margin:0;padding:0}
html,body{width:1200px;height:2904px;overflow:hidden}
body{font-family:"Montserrat",Arial,sans-serif;color:var(--ink);background:var(--white);position:relative}
section,header,footer{position:absolute;left:0;width:1200px}

/* HERO */
.hero{top:0;height:660px;overflow:hidden}
.hero-photo{position:absolute;inset:0;background:linear-gradient(100deg,#5a5d60 0%,#6f7275 35%,#9a9c9d 60%,#5c5f62 100%)}
.hero-shade{position:absolute;inset:0;background:linear-gradient(90deg,rgba(40,42,45,.55) 0%,rgba(40,42,45,.25) 55%,rgba(40,42,45,0) 100%)}
.nav{position:absolute;top:36px;left:60px;right:60px;height:50px;display:flex;align-items:center;justify-content:space-between}
.brand{display:flex;align-items:center;gap:12px}
.brand-mark{width:34px;height:34px;background:var(--orange)}
.brand-name{font-weight:800;font-size:22px;letter-spacing:.5px;color:var(--white);line-height:1}
.menu{display:flex;gap:42px;list-style:none}
.menu li{font-size:12px;font-weight:600;letter-spacing:.6px;color:var(--white)}
.hero-copy{position:absolute;left:60px;top:138px;width:580px;text-align:center;color:var(--white)}
.hero-title{font-size:38px;font-weight:700;color:var(--orange);letter-spacing:.5px}
.hero-sub{font-size:20px;font-weight:400;margin-top:6px}
.hero-badge{width:126px;height:126px;border-radius:50%;background:var(--orange);margin:42px auto 0;display:flex;align-items:center;justify-content:center;box-shadow:0 0 0 10px rgba(247,147,30,.25)}
.hero-lead{font-size:22px;font-weight:500;margin-top:34px;text-transform:uppercase;line-height:1.3}
.hero-tag{font-size:14px;opacity:.85;margin-top:10px}
.btn{display:inline-block;font-weight:700;font-size:15px;letter-spacing:.6px;text-transform:uppercase;padding:17px 36px;border-radius:3px}
.btn-orange{background:var(--orange);color:var(--white);margin-top:36px}
.btn-white{background:var(--white);color:var(--blue)}

/* WHY */
.why{top:660px;height:692px;background:var(--sky)}
.section-title{text-align:center;font-size:36px;font-weight:600;letter-spacing:.5px;text-transform:uppercase}
.why .section-title{padding-top:62px;color:var(--navy)}
.why .section-title em{font-style:normal;color:var(--orange)}
.title-rule{width:760px;height:1px;background:var(--line);margin:32px auto 0}
.usp-grid{position:absolute;top:190px;left:150px;width:940px;display:grid;grid-template-columns:1fr 1fr;column-gap:70px;row-gap:60px}
.usp{display:flex;gap:22px}
.usp-icon{flex:0 0 58px;height:58px;display:flex;align-items:flex-start;justify-content:center}
.usp h3{font-size:19px;font-weight:700;color:var(--navy);text-transform:uppercase;line-height:1.25}
.usp p{font-size:14px;color:#4c5560;margin-top:6px;line-height:1.45}

/* HOW */
.how{top:1352px;height:680px;background:var(--ink)}
.how .section-title{padding-top:74px;color:var(--white);font-weight:500;line-height:1.25}
.how .section-title strong{display:block;color:var(--green);font-weight:700}
.timeline{position:absolute;top:300px;left:120px;width:960px;height:320px}
.timeline-track{position:absolute;left:0;right:0;top:80px;height:2px;background:#3e4246}
.step{position:absolute;top:0;width:220px;margin-left:-110px;text-align:center}
.step-icon{height:70px;display:flex;align-items:flex-end;justify-content:center}
.step-dot{width:22px;height:22px;border-radius:50%;background:var(--blue);border:4px solid var(--ink);margin:0 auto;box-shadow:0 0 0 2px var(--blue)}
.step-drop{width:2px;height:36px;background:#3e4246;margin:0 auto}
.step h4{font-size:17px;font-weight:700;color:var(--blue);text-transform:uppercase;line-height:1.25;margin-top:14px}
.step p{font-size:14px;color:#b9bec3;margin-top:8px;line-height:1.45}

/* CTA */
.cta{top:2032px;height:152px;background:var(--blue);display:flex;align-items:center;justify-content:space-between;padding:0 120px}
.cta h2{font-size:18px;font-weight:700;color:var(--white);text-transform:uppercase}
.cta p{font-size:15px;color:var(--white);margin-top:6px;line-height:1.4}

/* REVIEWS */
.reviews{top:2184px;height:448px;background:var(--white)}
.reviews-head{text-align:center;padding-top:30px}
.reviews-head small{font-size:14px;color:var(--grey);display:block}
.reviews-head h2{font-size:32px;font-weight:500;margin-top:4px}
.summary{position:absolute;left:60px;top:140px;width:180px;height:170px;border:1px solid var(--line);padding:22px 18px}
.summary h3{font-size:18px;font-weight:600}
.summary .note{font-size:11px;color:var(--grey);margin-top:6px}
.summary .link{font-size:11px;color:var(--grey);margin-top:24px;border-top:1px solid var(--line);padding-top:12px}
.stars{display:flex;gap:3px;margin-top:10px}
.star{width:15px;height:15px;background:var(--green)}
.review-list{position:absolute;left:300px;top:110px;width:840px;display:grid;grid-template-columns:repeat(3,1fr);column-gap:40px}
.review{border-top:1px solid var(--line);padding-top:18px}
.review .stars{margin-top:0}
.review h3{font-size:22px;font-weight:600;line-height:1.2;margin-top:12px}
.review p{font-size:12px;color:#5b636b;margin-top:10px;line-height:1.5}
.review .who{font-size:11px;color:var(--grey);margin-top:12px;border-top:1px solid var(--line);padding-top:10px}
.pager{position:absolute;top:370px;left:0;right:0;display:flex;justify-content:center;gap:14px}
.pager span{width:34px;height:34px;border-radius:50%;border:1px solid var(--line);display:flex;align-items:center;justify-content:center}

/* FOOTER */
.footer{top:2632px;height:272px;background:var(--ink);color:var(--white)}
.footer-col{position:absolute;top:56px}
.footer-col h4{font-size:15px;font-weight:700;text-transform:uppercase;margin-bottom:16px}
.footer-col.follow h4{text-transform:none;font-weight:500}
.footer-col p{font-size:14px;line-height:1.9;color:#d0d3d6}
.socials{display:flex;gap:34px;margin-top:6px}
.social{display:flex;align-items:center;gap:8px;font-size:13px;color:#d0d3d6}
.social i{width:12px;height:12px;border-radius:50%;background:#d0d3d6;display:block}
</style>
</head>
<body>

<header class="hero">
  <div class="hero-photo" role="img" aria-label="Photo of gloved hands opening a smartphone with repair tools on a grey workbench"></div>
  <div class="hero-shade"></div>
  <nav class="nav">
    <div class="brand"><span class="brand-mark"></span><span class="brand-name">GADGET HAVEN</span></div>
    <ul class="menu">
      <li>WHY GADGET HAVEN</li>
      <li>HOW IT WORKS</li>
      <li>CUSTOMER REVIEWS</li>
      <li>CONTACT</li>
    </ul>
  </nav>
  <div class="hero-copy">
    <h1 class="hero-title">BROKEN PHONE OR TABLET?</h1>
    <p class="hero-sub">We are the solution to your problems</p>
    <div class="hero-badge">
      <svg width="52" height="60" viewBox="0 0 52 60"><rect x="8" y="4" width="30" height="52" fill="none" stroke="#fff" stroke-width="4"/><path d="M8 4 L26 10 L26 58 L8 56 Z" fill="#fff"/><circle cx="22" cy="32" r="2.5" fill="#f7931e"/></svg>
    </div>
    <p class="hero-lead">We come to your<br>doorstep</p>
    <p class="hero-tag">The quickest way to repair your device</p>
    <a class="btn btn-orange">Request a repair</a>
  </div>
</header>

<section class="why">
  <h2 class="section-title">Why <em>Gadget Haven?</em></h2>
  <div class="title-rule"></div>
  <div class="usp-grid">
    <div class="usp">
      <div class="usp-icon"><svg width="54" height="40" viewBox="0 0 54 40"><circle cx="14" cy="10" r="7" fill="#1d3557"/><circle cx="40" cy="10" r="7" fill="#1e8ff5"/><path d="M2 36c0-10 6-16 12-16s12 6 12 16z" fill="#1d3557"/><path d="M28 36c0-10 6-16 12-16s12 6 12 16z" fill="#1e8ff5"/></svg></div>
      <div><h3>Professional service on location.</h3><p>Don't ship to us we will come to you!</p></div>
    </div>
    <div class="usp">
      <div class="usp-icon"><svg width="46" height="48" viewBox="0 0 46 48"><circle cx="23" cy="16" r="12" fill="#1e8ff5"/><path d="M5 46c0-12 8-18 18-18s18 6 18 18z" fill="#1d3557"/><path d="M9 18a14 14 0 0 1 28 0" fill="none" stroke="#1d3557" stroke-width="3"/><rect x="5" y="16" width="6" height="10" rx="2" fill="#1d3557"/><rect x="35" y="16" width="6" height="10" rx="2" fill="#1d3557"/></svg></div>
      <div><h3>12 hour call center</h3><p>Backed by a professional call center open 12 hours a day and open on a Saturday as well</p></div>
    </div>
    <div class="usp">
      <div class="usp-icon"><svg width="44" height="44" viewBox="0 0 44 44"><circle cx="22" cy="22" r="20" fill="#1e8ff5"/><text x="22" y="30" text-anchor="middle" font-family="Montserrat,Arial,sans-serif" font-weight="700" font-size="22" fill="#fff">€</text></svg></div>
      <div><h3>Clear pricing upfront.</h3><p>No hidden cost.</p></div>
    </div>
    <div class="usp">
      <div class="usp-icon"><svg width="40" height="52" viewBox="0 0 40 52"><path d="M10 30 L4 50 L14 45 L20 52 L22 34Z" fill="#1d3557"/><path d="M30 30 L36 50 L26 45 L20 52 L18 34Z" fill="#1d3557"/><circle cx="20" cy="18" r="16" fill="#1e8ff5"/><circle cx="20" cy="18" r="9" fill="#fff"/></svg></div>
      <div><h3>Repair is done by certified engineers</h3><p>Backed by a professional repair center with more then 12 years of experience.</p></div>
    </div>
    <div class="usp">
      <div class="usp-icon"><svg width="58" height="38" viewBox="0 0 58 38"><rect x="2" y="6" width="34" height="22" fill="#1e8ff5"/><path d="M36 12h12l8 9v7H36z" fill="#1d3557"/><circle cx="12" cy="30" r="6" fill="#1d3557" stroke="#e4f3fa" stroke-width="3"/><circle cx="46" cy="30" r="6" fill="#1d3557" stroke="#e4f3fa" stroke-width="3"/></svg></div>
      <div><h3>Next business-day repair.</h3></div>
    </div>
    <div class="usp">
      <div class="usp-icon"><svg width="44" height="50" viewBox="0 0 44 50"><path d="M22 2 L40 8 V24 C40 36 32 44 22 48 C12 44 4 36 4 24 V8Z" fill="#1e8ff5"/><path d="M13 25 L20 32 L32 18" fill="none" stroke="#fff" stroke-width="4"/></svg></div>
      <div><h3>1 year warranty on the repair.</h3><p>We offer lightening fast turnarounds. No hassle. Guaranteed!</p></div>
    </div>
  </div>
</section>

<section class="how">
  <h2 class="section-title">How it works.<strong>We come to you</strong></h2>
  <div class="timeline">
    <div class="timeline-track"></div>
    <div class="step" style="left:110px">
      <div class="step-icon"><svg width="40" height="56" viewBox="0 0 40 56"><rect x="4" y="2" width="32" height="52" rx="4" fill="none" stroke="#1e8ff5" stroke-width="3"/><circle cx="20" cy="46" r="3" fill="#1e8ff5"/></svg></div>
      <div class="step-drop"></div><div class="step-dot"></div>
      <h4>Tell us the problem.</h4><p>Choose your device and repair job</p>
    </div>
    <div class="step" style="left:370px">
      <div class="step-icon"><svg width="62" height="50" viewBox="0 0 62 50"><rect x="2" y="16" width="36" height="22" fill="#1e8ff5"/><path d="M38 22h12l8 9v7H38z" fill="#1e8ff5"/><circle cx="12" cy="40" r="6" fill="#1c1c1c" stroke="#1e8ff5" stroke-width="3"/><circle cx="48" cy="40" r="6" fill="#1c1c1c" stroke="#1e8ff5" stroke-width="3"/><circle cx="50" cy="8" r="7" fill="#3cc23c"/><path d="M46 8l3 3 5-6" fill="none" stroke="#fff" stroke-width="2"/></svg></div>
      <div class="step-drop"></div><div class="step-dot"></div>
      <h4>Place the order.</h4><p>Get a callback within the hour.</p>
    </div>
    <div class="step" style="left:630px">
      <div class="step-icon"><svg width="54" height="52" viewBox="0 0 54 52"><rect x="2" y="8" width="50" height="42" rx="3" fill="none" stroke="#1e8ff5" stroke-width="3"/><rect x="2" y="8" width="50" height="12" fill="#1e8ff5"/><rect x="12" y="2" width="4" height="12" fill="#1e8ff5"/><rect x="38" y="2" width="4" height="12" fill="#1e8ff5"/><path d="M18 34l6 6 12-12" fill="none" stroke="#3cc23c" stroke-width="4"/></svg></div>
      <div class="step-drop"></div><div class="step-dot"></div>
      <h4>Set date and location</h4><p>We receive your order and confirm appointment</p>
    </div>
    <div class="step" style="left:880px">
      <div class="step-icon"><svg width="50" height="50" viewBox="0 0 50 50"><path d="M30 4a12 12 0 0 0-12 15L4 33l8 8 14-14A12 12 0 0 0 46 16l-7 7-8-8 7-7a12 12 0 0 0-8-4z" fill="#1e8ff5"/></svg></div>
      <div class="step-drop"></div><div class="step-dot"></div>
      <h4>We fix your device</h4><p>We will come to you and fix your device</p>
    </div>
  </div>
</section>

<section class="cta">
  <div>
    <h2>Do you need a mobile phone repair?</h2>
    <p>Choose your device and repair job. We will<br>come to you.</p>
  </div>
  <a class="btn btn-white">Request a repair</a>
</section>

<section class="reviews">
  <div class="reviews-head">
    <small>What our customers</small>
    <h2>Are Saying</h2>
  </div>
  <div class="summary">
    <h3>Excellent</h3>
    <div class="stars"><span class="star"></span><span class="star"></span><span class="star"></span><span class="star"></span><span class="star"></span></div>
    <p class="note">Based on 3 reviews</p>
    <p class="link">See all reviews →</p>
  </div>
  <div class="review-list">
    <article class="review">
      <div class="stars"><span class="star"></span><span class="star"></span><span class="star"></span><span class="star"></span><span class="star"></span></div>
      <h3>As good as advertised</h3>
      <p>"Great service at the right price."</p>
      <p class="who">Mia Janssen · 2 days ago</p>
    </article>
    <article class="review">
      <div class="stars"><span class="star"></span><span class="star"></span><span class="star"></span><span class="star"></span><span class="star"></span></div>
      <h3>Excellent service and good quality</h3>
      <p>"They came to my office, fixed my screen and I was back online within the hour."</p>
      <p class="who">Tom de Vries · 5 days ago</p>
    </article>
    <article class="review">
      <div class="stars"><span class="star"></span><span class="star"></span><span class="star"></span><span class="star"></span><span class="star"></span></div>
      <h3>Efficient and helpful in every way</h3>
      <p>"Friendly engineer, clear price, new battery fitted at my door. Would book again."</p>
      <p class="who">Eva Bakker · 1 week ago</p>
    </article>
  </div>
  <div class="pager">
    <span><svg width="10" height="12" viewBox="0 0 10 12"><path d="M8 1L2 6l6 5" fill="none" stroke="#3cc23c" stroke-width="2"/></svg></span>
    <span><svg width="10" height="12" viewBox="0 0 10 12"><path d="M2 1l6 5-6 5" fill="none" stroke="#3cc23c" stroke-width="2"/></svg></span>
  </div>
</section>

<footer class="footer">
  <div class="footer-col" style="left:120px">
    <h4>Contact us</h4>
    <p>1-888-555-0142<br>17 Quay Street, Dockside<br>hello@gadgethaven.example</p>
  </div>
  <div class="footer-col follow" style="left:640px">
    <h4>Follow Us</h4>
    <div class="socials">
      <span class="social"><i></i>Friends</span>
      <span class="social"><i></i>Updates</span>
      <span class="social"><i></i>Circles</span>
      <span class="social"><i></i>Photos</span>
    </div>
  </div>
</footer>

</body>
</html>
```